Digital Marketing Website Design

I need the homepage designed for my new digital marketing agency I am starting. The main goal for this homepage is to drive people to make an appointment for me to discuss their upcoming projects. Here are some examples of the layouts that I would like to emulate.
https://www.tallmarsh.com/
https://www.quillforge.com/
https://pebblenook.com/
https://drvenholt.com/
https://www.quietlyrooted.org/
My main focus is to attract leads that need help with running digital ads such as Chatterly ads and Finder Promos. I do offer other services like SEO and other things but the main focus is digital Ads.
The final design should communicate Orchid Digital is a Digital marketing strategist building predictable revenue for small businesses through digital ads, email and marketing automation.
Target Market(s)
30-55, business owners, income 100K+, ecommerce companies, etc.
Industry/Entity Type
Digital Marketing
Number of Pages Required
2 page
Font styles to use
Requirements
Must have
- An appealing look and feel set to drive people to make an appointment.
Logo
There needs to be a call to action button in the far right of the navigation
The same call to action in the navigation needs to be in each section on the homepage.
I need the homepage and an about us page.

```html
<!DOCTYPE html>
<html lang="en">
<head>
<meta charset="utf-8">
<title>Orchid Digital — Profitable Ad Campaigns</title>
<link href="https://fonts.googleapis.com/css2?family=Jost:wght@300;400;500;700;800&family=Lato:wght@400;700&display=swap" rel="stylesheet">
<style>
:root{
  --orange:#e85a0a;
  --orange-soft:#f0782f;
  --ink:#111111;
  --card:#151515;
  --paper:#ffffff;
  --mist:#dcd8d8;
  --grey-band:#e6e4e3;
  --muted:#bdbdbd;
}
*{margin:0;padding:0;box-sizing:border-box}
html,body{width:1200px;height:3997px;overflow:hidden}
body{position:relative;background:var(--paper);font-family:"Lato",sans-serif;color:var(--ink)}
.abs{position:absolute}

/* header */
.hero{left:0;top:0;width:1200px;height:745px;background:linear-gradient(100deg,#1a1410 0%,#3a2618 40%,#a2471a 75%,#d25a14 100%)}
.nav-bar{left:0;top:0;width:1200px;height:68px;background:rgba(0,0,0,.35)}
.brand-box{left:51px;top:0;width:269px;height:85px;background:#e8e6e4;border-radius:0 0 4px 4px;display:flex;align-items:center;justify-content:center}
.brand{font-family:"Jost",sans-serif;font-weight:800;font-size:22px;letter-spacing:.5px;color:var(--orange)}
.nav-link{top:24px;font-family:"Jost",sans-serif;font-size:21px;color:var(--paper)}
.hero-title{left:120px;top:240px;font-family:"Jost",sans-serif;font-weight:700;font-size:44px;line-height:54px;color:var(--paper)}
.hero-title .accent{color:var(--orange)}
.hero-text{left:124px;top:432px;width:400px;font-size:15px;line-height:25px;color:#eeeeee}
.btn{display:flex;align-items:center;justify-content:center;font-family:"Jost",sans-serif;font-size:13px;border-radius:3px;white-space:nowrap}
.btn-outline-light{border:1.5px solid var(--paper);color:var(--paper)}
.btn-orange{background:var(--orange);color:var(--paper)}
.btn-grey{background:#d9d9d9;color:var(--ink);border:1.5px solid #ffffff}
.hero-art{left:698px;top:280px;width:365px;height:250px;border-radius:4px;background:linear-gradient(135deg,rgba(255,255,255,.18),rgba(232,90,10,.6))}

/* partners */
.partners{left:0;top:745px;width:1200px;height:352px;background:var(--orange)}
.section-title-light{font-family:"Jost",sans-serif;font-weight:300;color:var(--paper)}
.partner-logo{top:935px;font-family:"Jost",sans-serif;font-size:21px;color:var(--paper)}

/* how it works */
.how-bg{left:0;top:1097px;width:1200px;height:530px;background:linear-gradient(180deg,#e9e8e7,#dcdad8)}
.how-orange{left:0;top:1627px;width:1200px;height:577px;background:var(--orange)}
.how-title{font-family:"Jost",sans-serif;font-weight:300;color:var(--orange);text-align:center;width:1200px;left:0}
.how-text{left:104px;width:992px;text-align:center;font-size:14.5px;line-height:25px;color:var(--ink)}
.step{top:1529px;width:248px;height:281px;background:var(--card);color:var(--paper)}
.step svg{position:absolute;left:64px;top:38px}
.step-text{position:absolute;left:16px;right:16px;font-size:14px;line-height:25px;text-align:justify}
.cta-text{left:85px;top:1936px;width:740px;font-family:"Jost",sans-serif;font-size:26px;line-height:32px;color:var(--paper)}

/* testimonials */
.voices{left:0;top:2204px;width:1200px;height:692px;background:linear-gradient(120deg,#2a2522,#3b3430 35%,#1f1b19 60%,#403833)}
.voices-tag{left:251px;top:2367px;width:202px;height:228px;background:var(--orange);padding:18px 28px;font-family:"Jost",sans-serif;font-size:37px;line-height:48px;color:var(--paper)}
.voices-photo{left:767px;top:2597px;width:234px;height:299px;background:linear-gradient(180deg,#8c8077,#5e534c)}
.voices-quote{left:767px;top:2816px;width:234px;text-align:center;font-family:"Jost",sans-serif;font-size:17px;line-height:22px;color:var(--orange-soft)}

/* quote */
.quote-band{left:0;top:2896px;width:1200px;height:554px;background:var(--mist)}
.quote-mark{font-family:"Jost",sans-serif;font-weight:800;font-size:110px;line-height:1;color:var(--orange)}
.quote-text{left:0;width:1200px;top:3136px;text-align:center;font-family:"Jost",sans-serif;font-size:31px;line-height:41px;color:var(--orange)}
.quote-by{left:0;width:1200px;top:3218px;text-align:center;font-family:"Jost",sans-serif;font-size:23px;color:#222}

/* footer */
.footer{left:0;top:3450px;width:1200px;height:547px;background:#000}
.foot-brand{left:75px;top:3517px;font-family:"Jost",sans-serif;font-weight:800;font-size:24px;color:var(--paper)}
.foot-head{font-family:"Jost",sans-serif;font-weight:500;font-size:18px;color:var(--orange)}
.foot-list{list-style:none;font-family:"Jost",sans-serif;font-size:18px;line-height:31.5px;color:var(--paper)}
.foot-line{font-family:"Jost",sans-serif;font-size:18px;color:var(--paper);display:flex;align-items:center;gap:14px}
.social{top:3695px;width:38px;height:38px;border-radius:50%;background:var(--orange)}
.field{background:#1c1c1c;border:1px solid #444;color:#6e6e6e;font-family:"Jost",sans-serif;font-size:16px;padding:4px 10px}
.send{left:1049px;top:3745px;width:45px;height:18px;background:var(--orange);color:#ffffff;font-family:"Jost",sans-serif;font-size:13px;display:flex;align-items:center;justify-content:center}
.divider{left:88px;top:3884px;width:1032px;height:3px;background:#3a3a3a}
.copyright{left:0;width:1200px;top:3918px;text-align:center;font-family:"Jost",sans-serif;font-size:18px;color:#d8d8d8}
</style>
</head>
<body>

<!-- Hero -->
<section class="abs hero" role="img" aria-label="Dim office photo with a warm orange tint behind the hero message"></section>
<div class="abs nav-bar"></div>
<div class="abs brand-box"><span class="brand">ORCHIDDIGITAL</span></div>
<nav>
  <a class="abs nav-link" style="left:492px">Home</a>
  <a class="abs nav-link" style="left:605px">About Us</a>
  <a class="abs nav-link" style="left:745px">How It Works</a>
  <a class="abs nav-link" style="left:934px">Schedule Appointment</a>
</nav>
<h1 class="abs hero-title">We Built <span class="accent">↘</span><br><span class="accent">Profitable Ad Campaigns</span><br>For small businesses</h1>
<p class="abs hero-text">The selling system that brings in Predictable revenue through digital ads, email, and marketing automation.</p>
<div class="abs btn btn-outline-light" style="left:122px;top:500px;width:180px;height:29px">Free Chatterly Ads Checklist</div>
<div class="abs btn btn-orange" style="left:311px;top:500px;width:162px;height:29px">Schedule an Appointment</div>
<div class="abs hero-art" role="img" aria-label="Illustration of a rising orange bar chart with an arrow and a confident figure standing on top"></div>

<!-- Partners -->
<section class="abs partners"></section>
<h2 class="abs section-title-light" style="left:0;width:1200px;text-align:center;top:805px;font-size:50px">Our Partners</h2>
<svg class="abs" style="left:154px;top:915px" width="40" height="70" viewBox="0 0 40 70"><polyline points="36,4 6,35 36,66" fill="none" stroke="#fff" stroke-width="4"/></svg>
<svg class="abs" style="left:1006px;top:915px" width="40" height="70" viewBox="0 0 40 70"><polyline points="4,4 34,35 4,66" fill="none" stroke="#fff" stroke-width="4"/></svg>
<span class="abs partner-logo" style="left:292px">[LOGO]</span>
<span class="abs partner-logo" style="left:435px">[LOGO]</span>
<span class="abs partner-logo" style="left:578px">[LOGO]</span>
<span class="abs partner-logo" style="left:721px">[LOGO]</span>
<span class="abs partner-logo" style="left:864px">[LOGO]</span>

<!-- How it works -->
<section class="abs how-bg" role="img" aria-label="Faded photo of a team working together in a bright office"></section>
<section class="abs how-orange"></section>
<h2 class="abs how-title" style="top:1150px;font-size:68px">How It Works…</h2>
<p class="abs how-text" style="top:1256px">At Orchid Digital Solutions we know that you want to have a profitable business. In order to do that, you need a strong system that can predictably bring in sales even in bad times. The problem is there is so much out there to wade through and so many people telling you what you should do which makes you feel frustrated, lost, and flat out stressed out. We believe that businesses with great products should get the customer.</p>
<p class="abs how-text" style="top:1357px">We understand the frustration which is why we are here to help you maneuver through the minutiae and create a system that flat out works.</p>
<h2 class="abs how-title" style="top:1426px;font-size:62px">Here’s how we do it:</h2>

<article class="abs step" style="left:213px">
  <svg width="120" height="105" viewBox="0 0 120 105" fill="none" stroke="#fff" stroke-width="3" stroke-linecap="round">
    <rect x="6" y="14" width="88" height="72" rx="6"/><line x1="6" y1="32" x2="94" y2="32"/>
    <line x1="26" y1="6" x2="26" y2="20"/><line x1="74" y1="6" x2="74" y2="20"/>
    <line x1="22" y1="48" x2="34" y2="48"/><line x1="46" y1="48" x2="58" y2="48"/><line x1="22" y1="64" x2="34" y2="64"/>
    <path d="M44 58l10 10M54 58l-10 10" stroke="#e85a0a"/>
    <circle cx="94" cy="82" r="17" fill="#151515"/><polyline points="94,73 94,82 101,86"/>
  </svg>
  <p class="step-text" style="top:170px">1.&nbsp;&nbsp;&nbsp; Schedule an appointment to go through the basics of what you need and to find out if we are a good fit to work together.</p>
</article>
<article class="abs step" style="left:480px">
  <svg width="120" height="105" viewBox="0 0 120 105" fill="none" stroke="#fff" stroke-width="3" stroke-linecap="round">
    <circle cx="60" cy="14" r="9"/><path d="M46 38c2-10 26-10 28 0"/>
    <circle cx="18" cy="62" r="8"/><path d="M6 84c2-10 22-10 24 0"/>
    <circle cx="102" cy="62" r="8"/><path d="M90 84c2-10 22-10 24 0"/>
    <path d="M20 30l-8 14M100 30l8 14M36 94c16 8 32 8 48 0"/>
    <g stroke="#e85a0a"><line x1="44" y1="78" x2="44" y2="70"/><line x1="54" y1="78" x2="54" y2="64"/><line x1="64" y1="78" x2="64" y2="58"/><line x1="74" y1="78" x2="74" y2="52"/><polyline points="40,64 56,54 66,58 80,44"/></g>
  </svg>
  <p class="step-text" style="top:196px">2.&nbsp;&nbsp;&nbsp; Work with our team to build out your customer journey and selling system</p>
</article>
<article class="abs step" style="left:746px">
  <svg width="120" height="105" viewBox="0 0 120 105" fill="none" stroke="#fff" stroke-width="3" stroke-linecap="round">
    <ellipse cx="60" cy="20" rx="16" ry="6"/><path d="M44 20v18c0 4 32 4 32 0V20"/><path d="M44 29c0 4 32 4 32 0"/>
    <ellipse cx="88" cy="42" rx="12" ry="5"/><path d="M76 42v16c0 4 24 4 24 0V42"/>
    <path d="M14 70h20c8 0 14 6 22 6h16M14 92h30c14 0 34-8 54-22"/>
    <g stroke="#e85a0a"><line x1="30" y1="4" x2="34" y2="12"/><line x1="96" y1="6" x2="90" y2="14"/><circle cx="66" cy="56" r="7"/></g>
  </svg>
  <p class="step-text" style="top:204px">3.&nbsp;&nbsp;&nbsp; Execute and enjoy the extra revenue!</p>
</article>

<p class="abs cta-text">So, schedule your appointment today. And in the meantime, checkout our Chatterly ads checklist. So you can stop any poor running campaigns and fill in the gaps where they are needed</p>
<div class="abs btn btn-grey" style="left:85px;top:2043px;width:178px;height:31px">Schedule an Appointment</div>
<div class="abs btn btn-outline-light" style="left:277px;top:2043px;width:197px;height:31px">Free Chatterly Ads Checklist</div>
<svg class="abs" style="left:875px;top:1940px" width="190" height="165" viewBox="0 0 190 165" fill="none" stroke="#fff" stroke-width="5" stroke-linecap="round" stroke-linejoin="round">
  <rect x="8" y="20" width="150" height="118" rx="10"/><line x1="8" y1="48" x2="158" y2="48"/>
  <line x1="44" y1="8" x2="44" y2="30"/><line x1="120" y1="8" x2="120" y2="30"/>
  <polyline points="52,92 78,118 140,40" stroke="#111" stroke-width="7"/>
  <circle cx="148" cy="128" r="28" fill="#e85a0a"/><polyline points="148,112 148,128 160,134"/>
</svg>

<!-- Testimonials -->
<section class="abs voices" role="img" aria-label="Collage of dimmed portrait photos of happy clients"></section>
<div class="abs voices-tag">What others are saying…</div>
<svg class="abs" style="left:251px;top:2594px" width="24" height="26" viewBox="0 0 24 26"><polygon points="0,0 24,0 0,26" fill="#e85a0a"/></svg>
<div class="abs voices-photo" role="img" aria-label="Bright portrait photo of a smiling client"></div>
<p class="abs voices-quote">“This is really cool”<br>-Marla</p>

<!-- Quote -->
<section class="abs quote-band"></section>
<span class="abs quote-mark" style="left:128px;top:3100px">“</span>
<span class="abs quote-mark" style="left:980px;top:3178px">”</span>
<p class="abs quote-text">Lorem ipsum dolor sit amet, consectetur adipiscing<br>elit. Sed eu ante feugiat lacus.</p>
<p class="abs quote-by">-anonymous</p>

<!-- Footer -->
<footer class="abs footer"></footer>
<div class="abs foot-brand">ORCHIDDIGITAL</div>
<div class="abs btn" style="left:75px;top:3584px;width:212px;height:36px;border:2px solid #e85a0a;color:#e85a0a;font-size:16px">Schedule an Appointment</div>
<div class="abs btn" style="left:75px;top:3639px;width:212px;height:36px;border:2px solid #ffffff;color:#ffffff;font-size:14px">Free Chatterly Ads Checklist</div>
<span class="abs social" style="left:77px"></span>
<span class="abs social" style="left:136px"></span>
<span class="abs social" style="left:194px"></span>
<span class="abs social" style="left:251px"></span>

<h4 class="abs foot-head" style="left:402px;top:3520px">NAVIGATE</h4>
<ul class="abs foot-list" style="left:402px;top:3546px">
  <li>Home</li><li>About Us</li><li>How It Works</li><li>Appointment</li><li>Our Team</li><li>Testimonials</li><li>Portfolio</li><li>Events</li><li>Contact</li>
</ul>
<h4 class="abs foot-head" style="left:616px;top:3520px">HELPFUL LINKS</h4>
<ul class="abs foot-list" style="left:616px;top:3546px">
  <li>Services</li><li>Supports</li><li>Terms &amp; Condition</li><li>Privacy Policy</li><li>Case studies</li>
</ul>
<h4 class="abs foot-head" style="left:841px;top:3520px">CONTACT US</h4>
<div class="abs foot-line" style="left:841px;top:3549px">
  <svg width="26" height="26" viewBox="0 0 24 24"><path d="M6 2l4 5-2 3c1 3 3 5 6 6l3-2 5 4-3 4C10 22 2 14 2 5z" fill="#fff"/></svg>info@orchiddigital.com
</div>
<div class="abs foot-line" style="left:841px;top:3582px">
  <svg width="26" height="20" viewBox="0 0 26 20"><rect x="1" y="2" width="24" height="16" fill="#fff"/><polyline points="1,2 13,11 25,2" fill="none" stroke="#000" stroke-width="2"/></svg>+10455500xxxxxx
</div>
<div class="abs field" style="left:855px;top:3632px;width:239px;height:27px">Your email address</div>
<div class="abs field" style="left:855px;top:3672px;width:239px;height:60px">Message</div>
<div class="abs send">Send</div>
<h4 class="abs foot-head" style="left:612px;top:3768px">VISIT OUR OFFICE</h4>
<div class="abs foot-line" style="left:618px;top:3798px">
  <svg width="18" height="24" viewBox="0 0 18 24"><path d="M9 1a8 8 0 0 1 8 8c0 6-8 14-8 14S1 15 1 9a8 8 0 0 1 8-8z" fill="#fff"/><circle cx="9" cy="9" r="3" fill="#000"/></svg>Lorem, Ipsum st. no.34, Dolor Sit Amet.
</div>
<div class="abs divider"></div>
<p class="abs copyright">Copyright © Orchiddigital, Ltd.&nbsp; All Right Reserved</p>

</body>
</html>
```